New, modern business card for growing audiology practice

We need a new business card for our audiology practice. Our logo and website have recently changed (more modern) and we want our business cards to reflect this change.
We conduct hearing tests, perform earwax removals, and fit & dispense hearing aids to our patients. We are a family owned practice in which the owner is the one who works directly with the patient. I have attached logos in various formats to use, as well as two ideas I found on this website; as well as a scanned copy of our current logo. Good luck!

Industry/Entity Type

Business

Contact Information for Business Card

Company name: Maplow Hearing Center
Provider name: Peter Mulvoy, Au.D. F/ISN
Phone number: (555) 318-6042
Address: 87 W. Linden Ave. Brookvale, OH 40117
email: maplowhearing@postvale.net
website: maplowhearing.com

Colors
000000
aaaaaa
dbdbdb
cacaca
9bcb3c
afd23c
cadf82
b1b1b1

Requirements
Must have
• My card must include information in the "details" section. In the attached images, I found a few that I liked and I would like to model after - "brisk tumblin'" and "Sound Wellness Center".
• Must be horizontal.
• Must include logos provided. I uploaded them in various file formats and various ways.
• Must match logo font, if possible, if not, please get as close as you can.
Nice to have
• I really like the idea of having a color on one side with just the logo and company name and the contact information and provider name on the other side. I also really like the idea of having the main color dominating on the logo/company side with accent of that same color on the contact side of the card.
Should not have
• Must not be vertical.

```html
<!DOCTYPE html>
<html lang="en">
<head>
<meta charset="utf-8">
<title>Maplow Hearing Center – Business Card</title>
<link rel="stylesheet" href="https://fonts.googleapis.com/css2?family=Open+Sans:wght@400;600&display=swap">
<style>
  :root {
    --backdrop: #2a2a2a;
    --card: #0b0b0b;
    --card-edge: #1a1a1a;
    --lime: #9bcb3c;
    --lime-bright: #afd23c;
    --text-light: #dbdbdb;
    --text-muted: #b1b1b1;
  }
  * { box-sizing: border-box; margin: 0; padding: 0; }
  html, body {
    width: 1200px; height: 900px; overflow: hidden;
    background: var(--backdrop);
    font-family: "Open Sans", Arial, sans-serif;
  }
  .sheet {
    width: 1200px; height: 900px;
    display: flex; flex-direction: column; align-items: center; justify-content: center;
    gap: 40px;
  }
  .card {
    width: 700px; height: 400px;
    background: var(--card);
    border-radius: 22px;
    border: 1px solid var(--card-edge);
    position: relative;
  }

  /* Contact side */
  .contact-side { display: flex; align-items: center; }
  .contact-side .brand {
    width: 330px; padding-left: 48px;
    display: flex; align-items: center; gap: 10px;
  }
  .brand-dot {
    width: 14px; height: 14px; border-radius: 50%;
    border: 2px solid var(--lime);
    flex-shrink: 0;
  }
  .brand-name {
    color: var(--text-light);
    font-size: 17px; font-weight: 400; letter-spacing: 0.5px;
    text-transform: uppercase;
    white-space: nowrap;
  }
  .divider {
    width: 2px; height: 200px; background: var(--lime);
  }
  .details { padding-left: 30px; }
  .provider-name {
    color: var(--lime-bright); font-size: 20px; font-weight: 600;
    text-transform: uppercase; letter-spacing: 0.3px;
    white-space: nowrap;
  }
  .provider-role { color: var(--text-light); font-size: 14px; margin-bottom: 14px; }
  .address { color: var(--text-light); font-size: 14px; line-height: 1.45; margin-bottom: 10px; }
  .contact-list { list-style: none; }
  .contact-list li {
    display: flex; align-items: center; gap: 10px;
    color: var(--text-light); font-size: 14px; line-height: 1.6;
  }
  .contact-list svg { width: 11px; height: 11px; flex-shrink: 0; fill: none; stroke: var(--lime); stroke-width: 2; }
  .web-accent { color: var(--lime-bright); font-weight: 600; }

  /* Logo side */
  .logo-side {
    display: flex; flex-direction: column; align-items: center; justify-content: center;
  }
  .logo-side .brand { display: flex; align-items: center; gap: 12px; margin-bottom: 18px; }
  .logo-side .brand-dot { width: 26px; height: 26px; border-width: 4px; }
  .logo-side .brand-name { font-size: 22px; }
  .accent-line {
    height: 2px; background: linear-gradient(90deg, transparent, var(--lime) 40%, var(--lime));
  }
  .accent-line.top { width: 340px; margin-bottom: 26px; }
  .web { color: var(--text-light); font-size: 14px; margin-bottom: 8px; }
  .accent-line.bottom { width: 220px; background: linear-gradient(90deg, var(--lime), var(--lime) 60%, transparent); }
</style>
</head>
<body>
<main class="sheet">
  <section class="card contact-side">
    <div class="brand">
      <span class="brand-dot"></span>
      <span class="brand-name">Maplow Hearing Center</span>
    </div>
    <div class="divider"></div>
    <div class="details">
      <p class="provider-name">Peter Mulvoy, Au.D. F/ISN</p>
      <p class="provider-role">Owner-Audiologist</p>
      <p class="address">87 W. Linden Ave.<br>Brookvale, OH 40117</p>
      <ul class="contact-list">
        <li><svg viewBox="0 0 12 12"><path d="M2 1.5 L4 1.5 L5 4 L3.8 5 Q5 7.5 7 8.2 L8 7 L10.5 8 L10.5 10 Q6 11 2.5 6.5 Q1.2 4 2 1.5 Z"/></svg><span>(555) 318-6042</span></li>
        <li><svg viewBox="0 0 12 12"><rect x="1" y="2.5" width="10" height="7"/><path d="M1 2.5 L6 6.5 L11 2.5"/></svg><span>maplowhearing@postvale.net</span></li>
        <li><svg viewBox="0 0 12 12"><circle cx="6" cy="6" r="4.8"/><path d="M1.2 6 H10.8 M6 1.2 Q3 6 6 10.8 M6 1.2 Q9 6 6 10.8"/></svg><span>www.<span class="web-accent">maplowhearing</span>.com</span></li>
      </ul>
    </div>
  </section>

  <section class="card logo-side">
    <div class="brand">
      <span class="brand-dot"></span>
      <span class="brand-name">Maplow Hearing Center</span>
    </div>
    <div class="accent-line top"></div>
    <p class="web">www.maplowhearing.com</p>
    <div class="accent-line bottom"></div>
  </section>
</main>
</body>
</html>
```